A billboard for Pine Hollow Construction size 36.5’ x 14.5’

Hi guys. We are purchasing a billboard and are looking for a design (size 36.5’ x 14.5’). Our slogan is "Quality you deserve, service you can count on". The goal of this billboard is brand recognition primarily letting people know we do roofs. Attached are logos that can be used if needed. Not necessarily all of them need to be used.

Target Market(s)

Residents in the local areas needing or thinking about a roof replacement

Industry/Entity Type

Roofing

Requirements
Must have
• Logo and services (roof replacement, gutters, siding, and snow removal)
Nice to have
• take a look at our website for ideas www.pinehollowconstruction.example

```html
<!DOCTYPE html>
<html lang="en">
<head>
<meta charset="utf-8">
<title>Pine Hollow Construction – Billboard</title>
<link href="https://fonts.googleapis.com/css2?family=Oswald:wght@400;500;700&family=Montserrat:wght@700;800&display=swap" rel="stylesheet">
<style>
  :root {
    --stage: #6f6f6f;
    --brand-red: #ec0a0a;
    --ink: #0a0a0a;
    --paper: #ffffff;
    --soft-white: #f4f6f8;
  }
  * { margin: 0; padding: 0; box-sizing: border-box; }
  html, body { width: 1200px; height: 1200px; overflow: hidden; }
  body { background: var(--stage); position: relative; }

  .billboard {
    position: absolute; left: 30px; top: 373px;
    width: 1140px; height: 453px;
    background: var(--paper);
  }

  .headline { position: absolute; left: 26px; top: 22px; width: 593px; }
  .headline__quality {
    font-family: "Oswald", sans-serif; font-weight: 700;
    font-size: 78px; line-height: 1; color: var(--brand-red);
    letter-spacing: -1.5px; transform: scaleX(0.86); transform-origin: left;
    white-space: nowrap;
  }
  .headline__service {
    font-family: "Oswald", sans-serif; font-weight: 700;
    font-size: 64px; line-height: 1; color: var(--ink);
    letter-spacing: -3px; transform: scaleX(0.89); transform-origin: left;
    white-space: nowrap; margin-top: 2px;
  }

  .brand {
    position: absolute; left: 680px; top: 30px; width: 440px; height: 130px;
    display: flex; align-items: center; gap: 16px;
  }
  .brand__mark { width: 26px; height: 26px; background: var(--brand-red); flex: none; }
  .brand__name {
    font-family: "Oswald", sans-serif; font-weight: 500;
    font-size: 44px; line-height: 1.05; color: var(--ink);
  }

  .services {
    position: absolute; left: 0; top: 180px; width: 1140px; height: 197px;
    background: var(--brand-red);
  }
  .service { position: absolute; top: 24px; width: 300px; margin-left: -150px; text-align: center; }
  .service__icon {
    width: 86px; height: 86px; margin: 0 auto;
    border: 3px solid var(--paper); border-radius: 10px;
    display: flex; align-items: center; justify-content: center;
  }
  .service__glyph { width: 62px; height: 62px; border-radius: 6px; background: rgba(255,255,255,0.85); }
  .service__label {
    font-family: "Oswald", sans-serif; font-weight: 400;
    font-size: 44px; line-height: 1; color: var(--paper);
    margin-top: 16px; letter-spacing: -1px; transform: scaleX(0.85);
    white-space: nowrap;
  }

  .contact-bar { position: absolute; left: 0; top: 377px; width: 1140px; height: 76px; }
  .contact-bar__band { position: absolute; left: 0; top: 0; }
  .phone {
    position: absolute; left: 44px; top: 0; height: 76px;
    display: flex; align-items: center; gap: 12px;
  }
  .phone__icon { flex: none; display: block; }
  .phone__number {
    font-family: "Montserrat", sans-serif; font-weight: 800;
    font-size: 58px; line-height: 1; color: var(--soft-white); letter-spacing: 1px;
  }
  .website {
    position: absolute; left: 584px; width: 540px; top: 0; height: 76px;
    display: flex; align-items: center; justify-content: center;
    font-family: "Montserrat", sans-serif; font-weight: 700;
    font-size: 28px; color: var(--ink);
  }
</style>
</head>
<body>
  <main class="billboard">
    <header class="headline">
      <h1 class="headline__quality">QUALITY YOU DESERVE</h1>
      <p class="headline__service">SERVICE YOU CAN COUNT ON</p>
    </header>

    <div class="brand">
      <span class="brand__mark"></span>
      <span class="brand__name">Pine Hollow<br>Construction</span>
    </div>

    <section class="services">
      <div class="service" style="left:198px">
        <div class="service__icon"><div class="service__glyph" role="img" aria-label="House roof with hammer icon"></div></div>
        <p class="service__label">ROOF REPLACEMENT</p>
      </div>
      <div class="service" style="left:491px">
        <div class="service__icon"><div class="service__glyph" role="img" aria-label="Gutter and downspout icon"></div></div>
        <p class="service__label">GUTTERS</p>
      </div>
      <div class="service" style="left:699px">
        <div class="service__icon"><div class="service__glyph" role="img" aria-label="House siding icon"></div></div>
        <p class="service__label">SIDING</p>
      </div>
      <div class="service" style="left:953px">
        <div class="service__icon"><div class="service__glyph" role="img" aria-label="Snow shovel over house icon"></div></div>
        <p class="service__label">SNOW REMOVAL</p>
      </div>
    </section>

    <footer class="contact-bar">
      <svg class="contact-bar__band" width="1140" height="76" viewBox="0 0 1140 76">
        <polygon points="0,0 532,0 572,38 532,76 0,76" fill="var(--ink)"/>
        <polygon points="532,0 542,0 582,38 542,76 532,76 572,38" fill="var(--brand-red)"/>
      </svg>
      <div class="phone">
        <svg class="phone__icon" width="40" height="40" viewBox="0 0 24 24" aria-hidden="true">
          <path d="M6.6 10.8a15.1 15.1 0 0 0 6.6 6.6l2.2-2.2a1 1 0 0 1 1-.25 11.4 11.4 0 0 0 3.6.57 1 1 0 0 1 1 1V20a1 1 0 0 1-1 1A17 17 0 0 1 3 4a1 1 0 0 1 1-1h3.5a1 1 0 0 1 1 1c0 1.25.2 2.45.57 3.57a1 1 0 0 1-.25 1z" fill="var(--brand-red)"/>
        </svg>
        <span class="phone__number">555-014-7720</span>
      </div>
      <div class="website">pinehollowconstruction.example</div>
    </footer>
  </main>
</body>
</html>
```